Business Card Design for Kidvale (Hires out childrens play areas)

Looking to have a business card designed for a company we just bought. The company rents out childrens play areas.

I have uploaded a couple of examples of the kind of business card style I like. Here are two more examples:

https://quorvastudio.nz/project/bright-romp-branding/
https://imgvaultcdn.com/design_img/8841052/302917/302917_5518203_8841052_b73e19a2_image.jpg

I think a white card will be best due to all the colours in the logo.

Size we require: 3.75" x 2.25" (horizontally orientated) with a 0.125" bleed

Uploaded is two versions of our logo.

Details for the card:
1. My name: Liam Verster
2. Title: Managing Director
3. Phone no: 021 563 417
4. Email: liam@kidvale.co.nz
5. URL: www.kidvale.co.nz
6. Address:
PO Box 318625
Fernlea, Auckland

Let me know if you need anything else.

Target Market(s)

Hospitals, doctors surgeries, bed shops, etc.

Contact Information for Business Card

Details for the card:
1. My name: Liam Verster
3. Phone no: 021 563 417
5. URL: www.kidvale.co.nz
6. Address:
PO Box 318625
Fernlea, Auckland

Requirements
Should not have
• Not too busy.

```html
<!DOCTYPE html>
<html lang="en">
<head>
<meta charset="utf-8">
<title>Kidvale – Business Card</title>
<link rel="stylesheet" href="https://fonts.googleapis.com/css2?family=Source+Sans+3:wght@400;600;700&display=swap">
<style>
  :root {
    --stage: #2b2b2d;
    --card-white: #f3f3f3;
    --brand-blue: #0a4f9e;
    --text-white: #ffffff;
  }
  html, body {
    margin: 0;
    padding: 0;
    width: 1200px;
    height: 923px;
    overflow: hidden;
    background: var(--stage);
    font-family: "Source Sans 3", "Myriad Pro", Arial, sans-serif;
  }
  .business-card {
    position: absolute;
    left: 100px;
    top: 161px;
    width: 1000px;
    height: 600px;
    background: var(--card-white);
    overflow: hidden;
  }
  .brand-lockup {
    position: absolute;
    left: 270px;
    top: 90px;
    display: flex;
    align-items: center;
    gap: 22px;
    color: var(--brand-blue);
  }
  .brand-mark {
    width: 74px;
    height: 74px;
    border-radius: 50%;
    background: var(--brand-blue);
  }
  .brand-name {
    font-size: 124px;
    font-weight: 700;
    line-height: 1;
    letter-spacing: 1px;
  }
  .rule-line {
    position: absolute;
    left: 0;
    right: 0;
    top: 318px;
    height: 4px;
    background: var(--brand-blue);
  }
  .info-band {
    position: absolute;
    left: 0;
    right: 0;
    top: 334px;
    bottom: 0;
    background: var(--brand-blue);
    color: var(--text-white);
  }
  .person {
    position: absolute;
    left: 120px;
    top: 86px;
  }
  .person-name {
    font-size: 50px;
    font-weight: 600;
    line-height: 1;
    margin: 0;
  }
  .person-title {
    font-size: 28px;
    font-weight: 400;
    margin: 6px 0 0 4px;
  }
  .band-divider {
    position: absolute;
    left: 486px;
    top: 40px;
    width: 2px;
    height: 180px;
    background: var(--text-white);
  }
  .contact-list {
    position: absolute;
    left: 536px;
    top: 38px;
    margin: 0;
    padding: 0;
    list-style: none;
    font-size: 26px;
    line-height: 32px;
  }
  .contact-item {
    display: flex;
    align-items: flex-start;
    gap: 14px;
  }
  .contact-icon {
    flex: none;
    width: 24px;
    height: 24px;
    margin-top: 5px;
  }
  .contact-item.address .contact-text span { display: block; }
</style>
</head>
<body>
  <section class="business-card" aria-label="Kidvale business card">
    <div class="brand-lockup">
      <span class="brand-mark" aria-hidden="true"></span>
      <span class="brand-name">Kidvale</span>
    </div>

    <div class="rule-line"></div>

    <div class="info-band">
      <div class="person">
        <p class="person-name">Liam Verster</p>
        <p class="person-title">Managing Director</p>
      </div>

      <div class="band-divider"></div>

      <ul class="contact-list">
        <li class="contact-item phone">
          <svg class="contact-icon" viewBox="0 0 24 24" aria-hidden="true">
            <rect width="24" height="24" rx="4" fill="#fff"/>
            <path d="M7 5l3 3-1.5 2c1 2 2.5 3.5 4.5 4.5l2-1.5 3 3-2 2.5C10 18 6 14 4.5 7.5z" fill="#0a4f9e"/>
          </svg>
          <span class="contact-text">021 563 417</span>
        </li>
        <li class="contact-item email">
          <svg class="contact-icon" viewBox="0 0 24 24" aria-hidden="true">
            <rect width="24" height="24" rx="4" fill="#fff"/>
            <rect x="4" y="7" width="16" height="11" fill="none" stroke="#0a4f9e" stroke-width="2"/>
            <path d="M4 7l8 6 8-6" fill="none" stroke="#0a4f9e" stroke-width="2"/>
          </svg>
          <span class="contact-text">liam@kidvale.co.nz</span>
        </li>
        <li class="contact-item web">
          <svg class="contact-icon" viewBox="0 0 24 24" aria-hidden="true">
            <rect width="24" height="24" rx="4" fill="#fff"/>
            <circle cx="12" cy="12" r="7" fill="none" stroke="#0a4f9e" stroke-width="2"/>
            <ellipse cx="12" cy="12" rx="3" ry="7" fill="none" stroke="#0a4f9e" stroke-width="1.5"/>
            <path d="M5 12h14" stroke="#0a4f9e" stroke-width="1.5"/>
          </svg>
          <span class="contact-text">www.kidvale.co.nz</span>
        </li>
        <li class="contact-item address">
          <svg class="contact-icon" viewBox="0 0 24 24" aria-hidden="true">
            <rect width="24" height="24" rx="4" fill="#fff"/>
            <path d="M12 20s-6-6-6-10a6 6 0 0 1 12 0c0 4-6 10-6 10z" fill="#0a4f9e"/>
            <circle cx="12" cy="10" r="2.2" fill="#fff"/>
          </svg>
          <span class="contact-text"><span>PO Box 318625</span><span>Fernlea, Auckland</span></span>
        </li>
      </ul>
    </div>
  </section>
</body>
</html>
```